QUOTE Graphics for Summer Challenge

I would like to put these quotes over one of the pictures attached; For Instagram, use new size: 4:5 (1080 x 1350 pixels). One Quote per picture, and I want the quote to be bold or easy to read as well. I provided a few reference graphics that I really like as examples below.
All of the pictures are attached; you can pick any photo and add one quote to it; but no stock photography
All the quotes are in the attached WORD document

```html
<!DOCTYPE html>
<html lang="en">
<head>
<meta charset="UTF-8">
<title>Summer Challenge Quote Graphics</title>
<link rel="stylesheet" href="https://fonts.googleapis.com/css2?family=Oswald:wght@700&family=Poppins:wght@300;400;600;800&display=swap">
<style>
  :root {
    --page: #ffffff;
    --navy-overlay: rgba(22, 40, 66, 0.88);
    --slate-overlay: rgba(48, 52, 58, 0.72);
    --white: #ffffff;
    --ink: #111111;
    --sky-top: #7aaed6;
    --sky-mid: #b7d4ea;
    --water: #3a9bd0;
    --water-deep: #2876b0;
    --hill: #5c6a3e;
    --deck: #d9cfbd;
  }
  * { margin: 0; padding: 0; box-sizing: border-box; }
  html, body { width: 1200px; height: 1045px; overflow: hidden; background: var(--page); }
  .board { position: relative; width: 1200px; height: 1045px; font-family: "Poppins", sans-serif; }
  .post { position: absolute; width: 356px; height: 445px; overflow: hidden; }
  .photo { position: absolute; inset: 0; }
  .headline {
    font-family: "Poppins", sans-serif; font-weight: 800; text-transform: uppercase;
    font-size: 20.5px; line-height: 1.24; letter-spacing: 0.1px;
  }
  .body-copy { font-weight: 300; font-size: 16px; line-height: 1.36; }

  /* post 1 */
  .post--scale-gown { left: 41px; top: 50px; }
  .post--scale-gown .photo {
    background: linear-gradient(180deg, var(--hill) 0%, #7b8a52 30%, var(--water-deep) 34%, var(--water) 70%, #5fb4dd 100%);
  }
  .post--scale-gown .caption-box {
    position: absolute; left: 146px; top: 242px; right: 0; bottom: 0;
    background: var(--navy-overlay); color: var(--white); padding: 16px 8px 0 18px;
  }
  .post--scale-gown .body-copy { margin-top: 8px; }

  /* post 2 */
  .post--bloated { left: 423px; top: 51px; }
  .post--bloated .photo {
    background: linear-gradient(180deg, var(--sky-top) 0%, #9cc4e3 40%, var(--sky-mid) 66%, #8fa07a 70%, #7ec3e6 76%, #a9daf1 92%, var(--deck) 100%);
  }
  .post--bloated .caption {
    position: absolute; left: 19px; top: 17px; right: 20px; color: var(--white);
  }
  .post--bloated .headline-condensed {
    font-family: "Oswald", sans-serif; font-weight: 700; text-transform: uppercase;
    font-size: 28px; line-height: 1.06;
  }
  .post--bloated .body-copy { margin-top: 8px; font-size: 15.5px; line-height: 1.32; }

  /* post 3 */
  .post--scale-pool { left: 803px; top: 53px; }
  .post--scale-pool .photo {
    background: linear-gradient(180deg, #8aa3bf 0%, #4f6a44 18%, #2f9ed8 24%, #3ab0e4 60%, #2b86ba 100%);
  }
  .post--scale-pool .caption-band {
    position: absolute; left: 0; right: 0; top: 330px; bottom: 0;
    background: var(--slate-overlay);
  }
  .post--scale-pool .accent-bar {
    position: absolute; left: 0; top: 336px; width: 7px; height: 99px; background: var(--white);
  }
  .post--scale-pool .headline {
    position: absolute; left: 25px; top: 336px; width: 190px; color: var(--white);
  }
  .post--scale-pool .body-copy {
    position: absolute; left: 226px; top: 332px; width: 124px; color: var(--white); line-height: 1.38;
  }

  /* post 4 */
  .post--jumpstart { left: 228px; top: 524px; }
  .post--jumpstart .photo {
    background: linear-gradient(180deg, var(--sky-mid) 0%, #c7dcec 18%, #6f7d5a 24%, #9aa888 36%, #4f9fd0 48%, #e6e9ec 62%, #cfd3d8 100%);
  }
  .post--jumpstart .caption-panel {
    position: absolute; left: 13px; top: 0; width: 172px; bottom: 0;
    background: linear-gradient(180deg, rgba(40,44,50,0) 0%, rgba(40,44,50,0.55) 14%, rgba(40,44,50,0.78) 40%, rgba(40,44,50,0.78) 78%, rgba(40,44,50,0.2) 100%);
    color: var(--white); padding: 122px 6px 0 18px;
  }
  .post--jumpstart .headline { font-weight: 600; font-size: 21px; }
  .post--jumpstart .body-copy { margin-top: 10px; font-weight: 400; line-height: 1.37; }

  /* post 5 */
  .post--summer-ready { left: 608px; top: 524px; }
  .post--summer-ready .photo {
    background: linear-gradient(180deg, #6c9ccc 0%, #9fc2de 50%, #b8cfde 68%, #4aa8d8 78%, #7dc3e4 86%, var(--deck) 92%, #d8c39c 100%);
  }
  .post--summer-ready .quote-card {
    position: absolute; left: 187px; top: 11px; width: 160px; height: 234px;
    background: var(--white); color: var(--ink); padding: 13px 4px 0 14px;
  }
  .post--summer-ready .headline { font-size: 19px; line-height: 1.28; }
  .post--summer-ready .body-copy {
    margin-top: 7px; font-weight: 400; font-size: 13px; line-height: 1.4;
    letter-spacing: -0.1px; white-space: nowrap;
  }
</style>
</head>
<body>
<main class="board">

  <article class="post post--scale-gown">
    <div class="photo" role="img" aria-label="Smiling woman in an olive mesh gown standing at the edge of an infinity pool with green hills behind"></div>
    <div class="caption-box">
      <h2 class="headline">The scale keeps climbing and nothing’s working?</h2>
      <p class="body-copy">This challenge is your lifeline. Comment SUN GLOW to join now!</p>
    </div>
  </article>

  <article class="post post--bloated">
    <div class="photo" role="img" aria-label="Woman in a leopard print bikini seated on a pool edge, looking over her shoulder under a clear blue sky"></div>
    <div class="caption">
      <h2 class="headline-condensed">Feeling bloated,<br>sluggish, and too big?</h2>
      <p class="body-copy">Your detox starts now. Comment<br>SUMMER to join the Sun Glow<br>Summer Slimdown</p>
    </div>
  </article>

  <article class="post post--scale-pool">
    <div class="photo" role="img" aria-label="Woman in a black swimsuit and aviator sunglasses leaning on the edge of a bright blue infinity pool"></div>
    <div class="caption-band"></div>
    <div class="accent-bar"></div>
    <h2 class="headline">The scale<br>keeps climbing<br>and nothing’s<br>working?</h2>
    <p class="body-copy">This challenge is your lifeline. Comment SUN GLOW to join now!</p>
  </article>

  <article class="post post--jumpstart">
    <div class="photo" role="img" aria-label="Smiling woman in an olive mesh gown posing on a pool deck with hills and loungers behind"></div>
    <div class="caption-panel">
      <h2 class="headline">Need a<br>jumpstart?</h2>
      <p class="body-copy">We’re detoxing, burning fat, and getting snatched. Comment SUN GLOW to join us on July 7th</p>
    </div>
  </article>

  <article class="post post--summer-ready">
    <div class="photo" role="img" aria-label="Woman in a black bikini and sunglasses in an infinity pool, arm resting on the edge"></div>
    <div class="quote-card">
      <h2 class="headline">Summer’s<br>here, but<br>your body<br>doesn’t feel<br>ready?</h2>
      <p class="body-copy">You’re not too late.<br>Comment SUMMER<br>to join the Sun Glow<br>Summer Slimdown</p>
    </div>
  </article>

</main>
</body>
</html>
```